Unique Editable Recipe Cards

Create 10 unique editable recipe cards. Please look at Quonly and see what Editable Recipe cards are popular to get an idea of what Cards will sell. Search for "Editable Recipe Cards". The final images will need to be editable in Canva.

```html
<!DOCTYPE html>
<html lang="en">
<head>
<meta charset="utf-8">
<title>Editable Recipe Card</title>
<link href="https://fonts.googleapis.com/css2?family=Allison&family=Poppins:wght@300;400&display=swap" rel="stylesheet">
<style>
  :root {
    --page-bg: #ece7e2;
    --card-bg: #fbfbfa;
    --ink: #3f3a38;
    --ink-soft: #5a5451;
    --rule: #8c8480;
    --note-bg: #e2e8df;
    --note-edge: #c9d2c5;
    --ring: #9a9a96;
    --art-teal: #7fb3b8;
    --art-wood: #c98a55;
    --art-cream: #f3e8d8;
  }
  * { box-sizing: border-box; margin: 0; padding: 0; }
  html, body { width: 1200px; height: 675px; overflow: hidden; }
  body {
    background: var(--page-bg);
    font-family: "Poppins", sans-serif;
    color: var(--ink);
    position: relative;
  }
  .recipe-card {
    position: absolute;
    left: 170px;
    top: 34px;
    width: 860px;
    height: 608px;
    background: var(--card-bg);
    box-shadow: 0 6px 24px rgba(60, 45, 35, 0.12);
    overflow: hidden;
  }
  .card-title {
    position: absolute;
    left: 50px;
    top: 40px;
    font-family: "Allison", cursive;
    font-weight: 400;
    font-size: 78px;
    line-height: 1;
    color: var(--ink);
    letter-spacing: 1px;
  }
  .recipe-meta {
    position: absolute;
    left: 66px;
    top: 140px;
    display: flex;
    align-items: center;
    gap: 16px;
    font-size: 14px;
    font-weight: 300;
    color: var(--ink-soft);
  }
  .meta-item { display: flex; align-items: center; gap: 6px; }
  .meta-item svg { width: 16px; height: 16px; }
  .title-rule {
    position: absolute;
    left: 150px;
    top: 190px;
    width: 175px;
    height: 1px;
    background: var(--rule);
  }
  .section-heading {
    font-family: "Allison", cursive;
    font-weight: 400;
    font-size: 50px;
    line-height: 1;
    color: var(--ink);
  }
  .instructions-heading {
    position: absolute;
    left: 58px;
    top: 212px;
  }
  .instructions-text {
    position: absolute;
    left: 80px;
    top: 262px;
    width: 390px;
    height: 346px;
    font-size: 14.5px;
    font-weight: 300;
    line-height: 31.5px;
    color: var(--ink);
    overflow: hidden;
  }
  .kitchen-art {
    position: absolute;
    left: 500px;
    top: 24px;
    width: 318px;
    height: 310px;
    background:
      radial-gradient(ellipse at 50% 80%, rgba(201,138,85,0.85) 0%, rgba(201,138,85,0) 45%),
      radial-gradient(ellipse at 50% 30%, rgba(127,179,184,0.8) 0%, rgba(127,179,184,0) 60%),
      radial-gradient(ellipse at center, var(--art-cream) 0%, rgba(243,232,216,0) 72%);
  }
  .ingredients-note {
    position: absolute;
    left: 508px;
    top: 372px;
    width: 312px;
    height: 186px;
    background: var(--note-bg);
    border: 1px solid var(--note-edge);
  }
  .note-rings {
    position: absolute;
    left: 14px;
    top: -9px;
    width: 284px;
    height: 18px;
  }
  .ingredients-heading {
    position: absolute;
    left: 18px;
    top: 20px;
    font-size: 42px;
  }
  .ingredient-list {
    position: absolute;
    left: 30px;
    top: 66px;
    list-style: none;
    font-size: 12px;
    font-weight: 300;
    line-height: 23px;
    color: var(--ink);
  }
  .ingredient-list li { display: flex; align-items: center; gap: 12px; }
  .ingredient-list li::before {
    content: "";
    width: 8px;
    height: 8px;
    border: 1px solid var(--ring);
    border-radius: 50%;
    flex: none;
  }
</style>
</head>
<body>
  <article class="recipe-card">
    <h1 class="card-title">Editable Recipe Card</h1>

    <div class="recipe-meta">
      <span class="meta-item">
        <svg viewBox="0 0 16 16" fill="none" stroke="#5a5451" stroke-width="1.2"><circle cx="8" cy="8" r="6.5"/><path d="M8 4.5V8l2.5 1.5"/></svg>
        Total time: 4 hours (includes cooling)
      </span>
      <span class="meta-item">
        <svg viewBox="0 0 16 16" fill="none" stroke="#5a5451" stroke-width="1.2"><path d="M4 1.5v13M2.5 1.5v4a1.5 1.5 0 0 0 3 0v-4M11 14.5v-13c-1.6 0-2.5 2-2.5 5s.9 3 2.5 3"/></svg>
        Yield: serves 12
      </span>
    </div>

    <div class="title-rule"></div>

    <h2 class="section-heading instructions-heading">Instructions</h2>
    <div class="instructions-text">
      <p>Preheat the oven to 350°F (177°C) and grease a 9x13-inch baking pan. I always use this glass pan</p>
      <p>Whisk the flour, baking powder, baking soda, salt, cinnamon, and pumpkin pie spice together in a large bowl. Set aside. Whisk the oil, eggs, brown sugar, granulated sugar, pumpkin, and vanilla extract together until combined. Pour the wet ingredients into the dry ingredients and use a mixer or whisk until completely combined. Batter will be thick.</p>
      <p>Spread batter into the prepared pan. Bake for 30-35 minutes. Baking times vary, so keep an eye on yours. The cake is done when a toothpick inserted in the center comes out clean. If you find the top or edges of the cake is/are browning too quickly in the oven, loosely cover it</p>
    </div>

    <div class="kitchen-art" role="img" aria-label="Watercolour illustration of a cosy kitchen with teal tiles, wooden cabinets, a table with stools and a window"></div>

    <section class="ingredients-note">
      <svg class="note-rings" viewBox="0 0 284 18" fill="none" stroke="#9a9a96" stroke-width="1.3">
        <ellipse cx="10" cy="9" rx="3" ry="7"/><ellipse cx="30" cy="9" rx="3" ry="7"/><ellipse cx="50" cy="9" rx="3" ry="7"/><ellipse cx="70" cy="9" rx="3" ry="7"/><ellipse cx="90" cy="9" rx="3" ry="7"/><ellipse cx="110" cy="9" rx="3" ry="7"/><ellipse cx="130" cy="9" rx="3" ry="7"/><ellipse cx="150" cy="9" rx="3" ry="7"/><ellipse cx="170" cy="9" rx="3" ry="7"/><ellipse cx="190" cy="9" rx="3" ry="7"/><ellipse cx="210" cy="9" rx="3" ry="7"/><ellipse cx="230" cy="9" rx="3" ry="7"/><ellipse cx="250" cy="9" rx="3" ry="7"/><ellipse cx="270" cy="9" rx="3" ry="7"/>
      </svg>
      <h2 class="section-heading ingredients-heading">Ingredients</h2>
      <ul class="ingredient-list">
        <li>2 cups (250g) all-purpose flour</li>
        <li>2 teaspoons baking powder</li>
        <li>1 teaspoon baking soda</li>
        <li>1 teaspoon salt</li>
        <li>1 and 1/2 teaspoons ground cinnamon</li>
      </ul>
    </section>
  </article>
</body>
</html>
```